BEACON CABS

Taxi card design

Need changes very slow in replying to my messages.

Target Market(s)

Customers

Industry/Entity Type

Taxi

Contact Information for Business Card

See previous design

Font styles to use
Sans Serif

Colors
A7469A
B969AE
D3A5CF
EDDBEB
F8F0F9
6B429C
8869AF
B7A5CE
E3DAEB
F3F0F8

Requirements
Nice to have
• We are in the business of looking after people, not just driving vehicles front
Should not have
• Front number 01632 480 480 needs to big big

```html
<!DOCTYPE html>
<html lang="en">
<head>
<meta charset="utf-8">
<title>Beacon Cabs – Business Card</title>
<link rel="stylesheet" href="https://fonts.googleapis.com/css2?family=Source+Sans+3:wght@400;700&family=Saira+Condensed:wght@700&display=swap">
<style>
  :root {
    --backdrop: #cbcbcb;
    --card: #020104;
    --violet-light: #a616f2;
    --violet-deep: #4a0fde;
    --violet-mid: #7a14f0;
    --ink: #0a0510;
    --muted: #5a5a60;
    --white: #ffffff;
  }
  * { margin: 0; padding: 0; box-sizing: border-box; }
  html, body {
    width: 1200px; height: 846px; overflow: hidden;
    background: var(--backdrop);
    font-family: "Source Sans 3", Arial, sans-serif;
  }
  .card {
    position: absolute; left: 346px; width: 508px; height: 290px;
    background: var(--card); overflow: hidden;
  }
  .card--front { top: 100px; }
  .card--back { top: 456px; }

  .brand-name {
    position: absolute; font-weight: 700; letter-spacing: 0.5px; white-space: nowrap;
  }
  .card--front .brand-name { left: 49px; top: 52px; font-size: 38px; color: var(--white); line-height: 1; }
  .tagline {
    position: absolute; left: 328px; top: 68px; font-size: 23px; font-weight: 700;
    background: linear-gradient(90deg, var(--violet-deep), var(--violet-light));
    -webkit-background-clip: text; background-clip: text; color: transparent; line-height: 1;
  }
  .contact-band {
    position: absolute; left: 0; top: 137px; width: 100%; height: 96px;
    background: radial-gradient(ellipse at 50% 55%, #b414f6 0%, #8e12f0 40%, var(--violet-deep) 100%);
  }
  .contact-list { position: absolute; top: 14px; list-style: none; }
  .contact-list--main { left: 50px; }
  .contact-list--lines { left: 325px; }
  .contact-list li {
    display: flex; align-items: center; height: 24.5px;
    font-size: 17.5px; color: var(--ink); white-space: nowrap;
  }
  .contact-list .icon { width: 19px; height: 19px; margin-right: 6px; flex: none; }
  .contact-list--main .icon { margin-right: 7px; }
  .address {
    position: absolute; left: 50px; top: 252px; font-size: 14.5px; color: var(--muted);
    letter-spacing: -0.2px; white-space: nowrap;
  }

  .card--back .brand-name {
    left: 55px; top: 68px; font-size: 76px; color: var(--violet-mid); line-height: 1;
  }
  .hotline { position: absolute; left: 55px; top: 171px; display: flex; align-items: center; }
  .hotline .icon { width: 38px; height: 39px; }
  .hotline-number {
    margin-left: 18px; font-family: "Saira Condensed", "Arial Narrow", sans-serif;
    font-weight: 700; font-size: 56px; line-height: 1; letter-spacing: 1px;
    background: linear-gradient(180deg, var(--violet-light), var(--violet-deep));
    -webkit-background-clip: text; background-clip: text; color: transparent;
  }
  .rule {
    position: absolute; left: 55px; top: 223px; width: 400px; height: 2px;
    background: linear-gradient(90deg, var(--violet-deep), var(--violet-light), var(--violet-deep));
  }
  .services {
    position: absolute; left: 57px; top: 232px; width: 396px;
    display: flex; justify-content: space-between; align-items: center;
    font-size: 15px; color: var(--muted); letter-spacing: 0.3px; white-space: nowrap;
  }
  .services .dot { font-size: 10px; }
</style>
</head>
<body>
<svg width="0" height="0" style="position:absolute" aria-hidden="true">
  <defs>
    <linearGradient id="iconFill" x1="0" y1="0" x2="1" y2="1">
      <stop offset="0" stop-color="#b016f4"/>
      <stop offset="1" stop-color="#4a0fde"/>
    </linearGradient>
    <symbol id="phone-tile" viewBox="0 0 24 24">
      <rect x="1" y="1" width="22" height="22" rx="4" fill="currentColor"/>
      <path d="M8.2 5.5c.5-.3 1.1-.2 1.4.3l1.3 2.2c.3.5.2 1-.2 1.4l-.9.8c.6 1.5 1.8 2.8 3.3 3.6l.9-.8c.4-.4 1-.4 1.4-.1l2.1 1.5c.5.3.6 1 .3 1.4l-.9 1.3c-.5.7-1.4 1-2.3.7-3.9-1.3-6.7-4.3-7.8-8.2-.2-.8.1-1.7.8-2.2z" fill="var(--tile-ink, #fff)"/>
    </symbol>
  </defs>
</svg>

<section class="card card--front">
  <div class="brand-name">Beacon Cabs</div>
  <div class="tagline">24/7 Service</div>

  <div class="contact-band">
    <ul class="contact-list contact-list--main">
      <li><svg class="icon" style="color:var(--ink);--tile-ink:#9a14f2"><use href="#phone-tile"/></svg>freephone: 0800 123 0 456</li>
      <li><svg class="icon" viewBox="0 0 24 24"><rect x="1.5" y="5" width="21" height="14" fill="none" stroke="#0a0510" stroke-width="2"/><path d="M1.5 5l10.5 8 10.5-8M1.5 19l8-7M22.5 19l-8-7" fill="none" stroke="#0a0510" stroke-width="2"/></svg>beaconcabs@mailbox.co.uk</li>
      <li><svg class="icon" viewBox="0 0 24 24" fill="none" stroke="#0a0510" stroke-width="1.8"><circle cx="12" cy="12" r="10"/><ellipse cx="12" cy="12" rx="4.5" ry="10"/><path d="M2 12h20M4 6.5h16M4 17.5h16"/></svg>www.northbycabs.co.uk</li>
    </ul>
    <ul class="contact-list contact-list--lines">
      <li><svg class="icon" style="color:var(--ink);--tile-ink:#8e12f0"><use href="#phone-tile"/></svg>01632 96 06 06</li>
      <li><svg class="icon" style="color:var(--ink);--tile-ink:#8e12f0"><use href="#phone-tile"/></svg>01632 96 07 07</li>
      <li><svg class="icon" style="color:var(--ink);--tile-ink:#8e12f0"><use href="#phone-tile"/></svg>01632 96 08 08</li>
    </ul>
  </div>

  <p class="address">Old Mill Hall&nbsp; / &nbsp;Market Lane&nbsp; / &nbsp;Northby NB1 4ZZ</p>
</section>

<section class="card card--back">
  <div class="brand-name">Beacon Cabs</div>
  <div class="hotline">
    <svg class="icon" viewBox="0 0 24 24"><rect x="1" y="1" width="22" height="22" rx="4" fill="url(#iconFill)"/><path d="M8.2 5.5c.5-.3 1.1-.2 1.4.3l1.3 2.2c.3.5.2 1-.2 1.4l-.9.8c.6 1.5 1.8 2.8 3.3 3.6l.9-.8c.4-.4 1-.4 1.4-.1l2.1 1.5c.5.3.6 1 .3 1.4l-.9 1.3c-.5.7-1.4 1-2.3.7-3.9-1.3-6.7-4.3-7.8-8.2-.2-.8.1-1.7.8-2.2z" fill="#020104"/></svg>
    <span class="hotline-number">01632 480 480</span>
  </div>
  <div class="rule"></div>
  <p class="services">
    <span>AIRPORT TRANSFERS</span><span class="dot">•</span><span>MINIBUSES</span><span class="dot">•</span><span>SCHOOL TRANSPORT</span>
  </p>
</section>
</body>
</html>
```